Digital Teaching Model

The primary goal would be to develop a new vision for the Digital Teaching Powerpt. I am attaching an older version called DT, I would like it updated to include our colors and our models with new images that make the presentation more relevant. I am also attaching brochures around the new curriculum. The Links below will give examples to the digital lessons: https://512.brevinotal.com/review/content/7c3d9a41-58b2-4f07-b6e1-2a9d0c4f8e17/review and https://512.brevinotal.com/review/content/4e81b6f2-0d93-47a5-8c2e-9f1a73d5b06c/review. the Digital teaching PWRPT should include some of these images and the color palet from the company brochure which is attached.
Education

```html
<!DOCTYPE html>
<html lang="en">
<head>
<meta charset="utf-8">
<title>Digital Teaching Model – Slides</title>
<link href="https://fonts.googleapis.com/css2?family=Barlow+Condensed:ital,wght@0,400;0,500;0,600;0,700;1,700&family=Roboto+Condensed:wght@400&display=swap" rel="stylesheet">
<style>
  :root{
    --stage:#202021;
    --paper:#ffffff;
    --orange:#ee844f;
    --yellow:#fcc32f;
    --slate:#5a5a5c;
    --navy:#1c5069;
    --ink:#1a1a1a;
    --title-grey:#575757;
    --brand-grey:#7a7a7a;
  }
  html,body{margin:0;padding:0}
  body{
    width:1200px;height:3110px;overflow:hidden;
    background:var(--stage);position:relative;
    font-family:"Barlow Condensed",sans-serif;
  }
  .slide{
    position:absolute;left:170px;width:860px;height:646px;
    background:var(--paper);overflow:hidden;
  }
  .slide--timeline{top:136px}
  .slide--book{top:866px}
  .slide--loop{top:1596px}
  .slide--lms{top:2328px}
  .slide svg.art{position:absolute;left:0;top:0;width:860px;height:646px}

  .label-arc{font-family:"Barlow Condensed",sans-serif;font-size:16px;font-weight:500;fill:var(--ink)}
  .label-arc .year{font-weight:700;font-style:italic}
  .hub-title{font-family:"Barlow Condensed",sans-serif;font-weight:700;font-size:27px;fill:var(--title-grey);text-anchor:middle;letter-spacing:.5px}
  .next-gen{font-family:"Barlow Condensed",sans-serif;font-weight:700;font-style:italic;font-size:16px;fill:var(--navy)}
  .brand-name{font-family:"Barlow Condensed",sans-serif;font-weight:500;font-size:26px;fill:var(--brand-grey)}
  .page-no{font-family:"Barlow Condensed",sans-serif;font-weight:500;font-size:16px;fill:#fff}

  .book-copy{
    position:absolute;left:42px;top:122px;width:430px;height:338px;
    border-top:2px solid var(--ink);border-bottom:2px solid var(--ink);
    box-sizing:border-box;padding:20px 12px 0 12px;
    font-family:"Roboto Condensed",sans-serif;font-size:11.2px;line-height:15.7px;
    color:var(--ink);text-align:justify;
  }
  .book-copy p{margin:0 0 15px}

  .band-title{font-family:"Barlow Condensed",sans-serif;font-weight:700;font-size:34px;fill:#fff;text-anchor:middle}
  .node-label{font-family:"Barlow Condensed",sans-serif;font-weight:500;font-size:17px;fill:#fff;text-anchor:middle}
  .lms-heading{font-family:"Barlow Condensed",sans-serif;font-weight:600;font-size:33px;fill:var(--navy)}
  .lms-item{font-family:"Barlow Condensed",sans-serif;font-weight:500;font-size:25px;fill:var(--ink)}
</style>
</head>
<body>

<!-- Slide 1: evolution timeline -->
<section class="slide slide--timeline">
  <svg class="art" viewBox="0 0 688 517" aria-label="Evolution of digital instructional tools">
    <defs>
      <radialGradient id="hubGlow" cx="50%" cy="55%" r="50%">
        <stop offset="0" stop-color="#d9d9db"/>
        <stop offset="1" stop-color="#ffffff"/>
      </radialGradient>
      <linearGradient id="photoTone" x1="0" y1="0" x2="1" y2="1">
        <stop offset="0" stop-color="#c9cfd6"/>
        <stop offset="1" stop-color="#7b8896"/>
      </linearGradient>
      <path id="arcLabs" d="M85,337 A62,62 0 0 1 150,245"/>
      <path id="arcBoards" d="M142,205 A68,68 0 0 1 238,109"/>
      <path id="arcClass" d="M276,82 A70,70 0 0 1 413,88"/>
      <path id="arcPrint" d="M472,94 A68,68 0 0 1 550,179"/>
      <path id="arcPlatforms" d="M564,236 A72,72 0 0 1 564,376"/>
    </defs>

    <ellipse cx="344" cy="290" rx="300" ry="250" fill="url(#hubGlow)"/>

    <!-- pointers -->
    <polygon points="160,262 224,306 160,350" fill="var(--orange)"/>
    <polygon points="232,128 259,225 166,206" fill="var(--orange)"/>
    <polygon points="296,110 344,187 392,110" fill="var(--orange)"/>
    <polygon points="456,128 429,221 522,206" fill="var(--yellow)"/>
    <polygon points="527,262 464,306 527,350" fill="var(--slate)"/>

    <!-- rings -->
    <g fill="none" stroke-width="3">
      <path d="M112,353 A54,54 0 0 1 130,253" stroke="var(--orange)"/>
      <path d="M143,180 A54,54 0 0 1 221,114" stroke="var(--orange)"/>
      <path d="M293,82 A54,54 0 0 1 395,82" stroke="var(--orange)"/>
      <path d="M466,110 A54,54 0 0 1 535,180" stroke="var(--yellow)"/>
      <path d="M566,255 A54,54 0 0 1 566,357" stroke="var(--slate)"/>
    </g>

    <!-- photo areas -->
    <circle cx="139" cy="306" r="48" fill="url(#photoTone)" role="img" aria-label="Photo: students working in a computer lab"/>
    <circle cx="194" cy="161" r="48" fill="#d9ddc8" role="img" aria-label="Photo: teacher presenting at an electronic whiteboard"/>
    <circle cx="344" cy="100" r="48" fill="#e3dcd2" role="img" aria-label="Photo: young pupils using computers in class"/>
    <circle cx="484" cy="161" r="48" fill="#cfe0e6" role="img" aria-label="Image: print and digital lesson screen"/>
    <circle cx="547" cy="306" r="48" fill="#c8d2d8" role="img" aria-label="Photo: classroom using a digital teaching platform"/>

    <!-- curved labels -->
    <text class="label-arc"><textPath href="#arcLabs">Computer Labs <tspan class="year">1985</tspan></textPath></text>
    <text class="label-arc"><textPath href="#arcBoards">Electronic Whiteboards <tspan class="year">2000</tspan></textPath></text>
    <text class="label-arc"><textPath href="#arcClass">In-class Computing <tspan class="year">2010</tspan></textPath></text>
    <text class="label-arc"><textPath href="#arcPrint">Print- Digital <tspan class="year">2012</tspan></textPath></text>
    <text class="label-arc"><textPath href="#arcPlatforms">Digital Teaching Platforms</textPath></text>
    <text class="next-gen" x="473" y="384">Next Gen</text>

    <!-- hub -->
    <circle cx="344" cy="308" r="100" fill="none" stroke="#444" stroke-width="2" stroke-dasharray="0.1 8" stroke-linecap="round"/>
    <g stroke-width="2" fill="#fff">
      <circle cx="271" cy="236" r="6" stroke="var(--orange)"/><circle cx="271" cy="236" r="2.5" fill="var(--orange)" stroke="none"/>
      <circle cx="344" cy="207" r="6" stroke="var(--orange)"/><circle cx="344" cy="207" r="2.5" fill="var(--orange)" stroke="none"/>
      <circle cx="415" cy="236" r="6" stroke="var(--yellow)"/><circle cx="415" cy="236" r="2.5" fill="var(--yellow)" stroke="none"/>
      <circle cx="242" cy="308" r="6" stroke="var(--orange)"/><circle cx="242" cy="308" r="2.5" fill="var(--orange)" stroke="none"/>
      <circle cx="445" cy="308" r="6" stroke="var(--slate)"/><circle cx="445" cy="308" r="2.5" fill="var(--slate)" stroke="none"/>
    </g>
    <text class="hub-title" x="344" y="276">EVOLUTION</text>
    <text class="hub-title" x="344" y="306">OF DIGITAL</text>
    <text class="hub-title" x="344" y="336">INSTRUCTIONAL</text>
    <text class="hub-title" x="344" y="366">TOOLS</text>

    <!-- footer wave -->
    <path d="M0,404 C150,388 260,398 400,442 C520,480 620,492 688,462" fill="none" stroke="var(--orange)" stroke-width="8"/>
    <rect x="78" y="461" width="12" height="12" fill="var(--orange)"/>
    <text class="brand-name" x="98" y="477">Lumora Learning</text>
  </svg>
</section>

<!-- Slide 2: book summary -->
<section class="slide slide--book">
  <svg class="art" viewBox="0 0 688 517">
    <defs>
      <linearGradient id="coverTone" x1="0" y1="0" x2="1" y2="1">
        <stop offset="0" stop-color="#2b4f9a"/>
        <stop offset="1" stop-color="#1a3472"/>
      </linearGradient>
    </defs>
    <rect x="424" y="52" width="230" height="375" fill="url(#coverTone)" role="img" aria-label="Photo: deep blue hardcover book standing upright"/>
    <path d="M0,428 C120,408 250,412 380,455 C450,478 520,500 688,505 V517 H0Z" fill="var(--slate)"/>
    <path d="M0,422 C120,400 260,405 420,455 C520,490 620,500 688,462" fill="none" stroke="var(--orange)" stroke-width="7"/>
    <text class="page-no" x="54" y="494">02</text>
  </svg>
  <div class="book-copy">
    <p>The Digital Teaching Platform contains a comprehensive curriculum of guided learning sequences that include applet activities, multimedia presentations, practice exercises, and activities. Before class the teacher uses planning tools to prepare; during class he uses multimedia to introduce a topic, an math tool to explore a mathematics concept, and practice exercises. After class, the teacher can review each student's progress, trends in the class performance, and begin the process for planning tomorrow's lessons.</p>
    <p>The platform provides powerful tools to the teacher for planning and managing lessons, customizing instruction to individuals, and providing quick feedback on all activities. It facilitates the management of groups of students without losing focus on individuals. It frees up the teacher for small group work and individual tutoring. In these ways, the platform respects the role of schools in today's society by teaching to standards and preparing students for high-stakes tests.</p>
    <p>At the same time, the Q4L Digital Teaching Platform deploys a social constructivist pedagogy and provides tools and content to build on that approach. It features open-ended explorations, student collaboration, shared work, and group discussion. In this way the platform goes beyond the standards and engages students in their learning, preparing them in a deep way for their place in a technology-rich society.</p>
  </div>
</section>

<!-- Slide 3: instructional loop -->
<section class="slide slide--loop">
  <svg class="art" viewBox="0 0 688 517">
    <rect x="0" y="0" width="688" height="58" fill="var(--navy)"/>
    <rect x="0" y="58" width="688" height="4" fill="#3a3a3c"/>
    <text class="band-title" x="344" y="46">Traditional LMS Instructional Loop</text>

    <!-- cycle arrows -->
    <g fill="none" stroke-linejoin="round" stroke-linecap="round">
      <path d="M287,188 C280,140 230,128 200,132 C170,136 150,155 146,176" stroke="var(--navy)" stroke-width="16"/>
      <path d="M287,188 C280,140 230,128 200,132 C170,136 150,155 146,176" stroke="#fff" stroke-width="11"/>
      <polygon points="122,152 106,196 168,197" fill="#fff" stroke="var(--navy)" stroke-width="2.5"/>
      <path d="M104,306 C110,350 160,366 190,364 C230,360 255,340 262,318" stroke="var(--navy)" stroke-width="16"/>
      <path d="M104,306 C110,350 160,366 190,364 C230,360 255,340 262,318" stroke="#fff" stroke-width="11"/>
      <polygon points="232,298 292,310 268,352" fill="#fff" stroke="var(--navy)" stroke-width="2.5"/>
    </g>

    <!-- nodes -->
    <g fill="var(--navy)">
      <path d="M53,233 H176 Q196,233 196,253 V289 H73 Q53,289 53,269 Z"/>
      <path d="M218,233 H341 Q361,233 361,253 V289 H238 Q218,289 218,269 Z"/>
      <path d="M405,233 H468 Q488,233 488,253 V289 H425 Q405,289 405,269 Z"/>
      <path d="M553,233 H615 Q635,233 635,253 V289 H573 Q553,289 553,269 Z"/>
    </g>
    <text class="node-label" x="124" y="257">Content</text>
    <text class="node-label" x="124" y="276">Management</text>
    <text class="node-label" x="289" y="267">Assessment</text>
    <text class="node-label" x="446" y="257">Grade</text>
    <text class="node-label" x="446" y="276">Book</text>
    <text class="node-label" x="594" y="267">SIS</text>

    <g fill="var(--navy)">
      <rect x="364" y="257" width="24" height="7"/>
      <polygon points="386,249 401,260.5 386,272"/>
      <rect x="505" y="257" width="30" height="7"/>
      <polygon points="507,249 492,260.5 507,272"/>
      <polygon points="533,249 548,260.5 533,272"/>
    </g>

    <path d="M0,428 C120,408 250,412 380,455 C450,478 520,500 688,505 V517 H0Z" fill="var(--slate)"/>
    <path d="M0,422 C120,400 260,405 420,455 C520,490 620,500 688,462" fill="none" stroke="var(--orange)" stroke-width="7"/>
    <text class="page-no" x="54" y="494">03</text>
  </svg>
</section>

<!-- Slide 4: traditional LMS -->
<section class="slide slide--lms">
  <svg class="art" viewBox="0 0 688 517">
    <rect x="0" y="0" width="688" height="58" fill="var(--navy)"/>
    <rect x="0" y="58" width="688" height="4" fill="#3a3a3c"/>
    <text class="band-title" x="344" y="46">Traditional LMS</text>

    <text class="lms-heading" x="77" y="176">Skinnerian Teaching Machines—ILS’s</text>

    <defs>
      <g id="tick">
        <circle cx="0" cy="0" r="9" fill="none" stroke="var(--navy)" stroke-width="2"/>
        <path d="M-4,0 L-1,4 L9,-8" fill="none" stroke="var(--navy)" stroke-width="2.6" stroke-linecap="round" stroke-linejoin="round"/>
      </g>
    </defs>
    <use href="#tick" x="88" y="221"/>
    <use href="#tick" x="88" y="255"/>
    <use href="#tick" x="88" y="289"/>
    <use href="#tick" x="88" y="324"/>
    <use href="#tick" x="88" y="358"/>
    <text class="lms-item" x="114" y="229">“Teacher Proof” Technology</text>
    <text class="lms-item" x="114" y="263">Closed Curriculum</text>
    <text class="lms-item" x="114" y="297">Fixed Map from Assessment to Curriculum</text>
    <text class="lms-item" x="114" y="332">Lab or Back of the Room</text>
    <text class="lms-item" x="114" y="366">One student only</text>

    <path d="M0,428 C120,408 250,412 380,455 C450,478 520,500 688,505 V517 H0Z" fill="var(--slate)"/>
    <path d="M0,422 C120,400 260,405 420,455 C520,490 620,500 688,462" fill="none" stroke="var(--orange)" stroke-width="7"/>
    <text class="page-no" x="54" y="494">04</text>
  </svg>
</section>

</body>
</html>
```